Design a Brochure for IT Cloud company

This is an open idea type brochure design. I will attach our logo so that there's relevance, and brochure text to be arranged and placed in arrangement that your design will produce.....Ideally I would like a tri-fold brochure if possible [login to view URL]

```html
<!DOCTYPE html>
<html lang="en">
<head>
<meta charset="utf-8">
<title>Nimbara Enterprise Systems – Tri-fold Brochure</title>
<link href="https://fonts.googleapis.com/css2?family=Open+Sans:wght@400;600;700&display=swap" rel="stylesheet">
<style>
:root{
  --page-bg:#e9eaec;
  --paper:#ffffff;
  --band:#4d4e50;
  --band-text:#ffffff;
  --ink:#4a4c4f;
  --ink-soft:#6a6c70;
  --heading:#3d3f42;
  --blue:#2a8bc4;
  --blue-deep:#1d73aa;
  --blue-light:#7cc0e4;
  --tick:#2a8bc4;
}
*{box-sizing:border-box;margin:0;padding:0}
html,body{width:1200px;height:1029px;overflow:hidden}
body{background:var(--page-bg);font-family:"Open Sans",Arial,sans-serif;color:var(--ink);font-size:10.6px;line-height:1.5}
.brochure{position:absolute;left:45px;top:48px;width:1110px;height:933px;display:flex;box-shadow:0 6px 24px rgba(0,0,0,.12)}
.panel{width:370px;height:100%;background:var(--paper);display:flex;flex-direction:column;position:relative}
.panel + .panel{border-left:1px solid #dfe1e4}
.band{background:var(--band);color:var(--band-text);font-weight:600;font-size:17px;padding:9px 24px;margin:0 0 12px}
.panel-body{padding:0 24px}
p{margin:0 0 8px}
.subhead{font-weight:600;font-size:13px;color:var(--heading);margin:2px 0 6px}
.bullets{list-style:none;margin:0 0 10px}
.bullets li{position:relative;padding-left:14px;margin-bottom:2px;text-transform:uppercase;font-size:10px}
.bullets li::before{content:"";position:absolute;left:2px;top:6px;width:5px;height:5px;border-radius:50%;background:var(--blue)}
.plain-list li{text-transform:none;font-size:10.6px}
.foot-strip{margin-top:auto;height:16px;background:linear-gradient(90deg,var(--blue-deep),var(--blue-light))}

/* middle panel */
.panel--feature{background:var(--paper)}
.feature-top{background:linear-gradient(160deg,var(--blue-deep) 0%,var(--blue) 45%,var(--blue-light) 100%);color:#fff;padding:26px 24px 18px}
.feature-title{display:flex;align-items:center;justify-content:space-between;margin-bottom:12px}
.feature-title h2{font-size:19px;font-weight:600;line-height:1.25;width:200px}
.vault{width:110px;height:96px;border-radius:6px;background:linear-gradient(135deg,#e4e6e9,#9ea3aa)}
.feature-top .subhead{color:#fff;font-size:14px}
.feature-top .bullets li::before{background:#fff}
.network{width:300px;height:210px;margin:26px auto 10px;border-radius:50%;background:radial-gradient(ellipse at center,#cfe7f5 0%,#eef2f5 55%,#ffffff 75%)}
.web{text-align:center;color:var(--blue);font-weight:600;font-size:13px;margin-bottom:18px}

/* right panel */
.ticks{list-style:none;margin:0 0 10px}
.ticks li{display:flex;gap:8px;align-items:flex-start;margin-bottom:5px}
.ticks svg{flex:none;margin-top:2px}
.ticks--short li{font-weight:600;color:var(--heading);margin-bottom:7px}
.cta{font-weight:600;color:var(--heading)}
</style>
</head>
<body>
<main class="brochure">

  <section class="panel panel--intro">
    <h2 class="band" style="margin-top:40px">Business Online</h2>
    <div class="panel-body">
      <p>Nimbara Enterprise Systems is a privately owned company that provides Cloud leading technology solutions across a wide range of industries throughout Australia and Asia Pacific.</p>
      <p>Based in beautiful Sydney, our business, structure and technology solutions are all designed to help customers meet their business objectives. We design, engineer and manage technology solutions through our specialist businesses which are Consulting Solutions, Integrated Solutions and Managed Services. Our Consulting and Service Delivery teams, based on a wealth of Technical and Business Knowledge, enable our customers to align their ICT programs with their business objectives.</p>
      <p>Your corporate data is safe and secure in two of Australia's premier datacentres, protected by technology and practices small businesses generally cannot afford.</p>
    </div>
    <h2 class="band" style="margin-top:8px">Our CORE Business</h2>
    <div class="panel-body">
      <ul class="bullets">
        <li>Cloud computing</li>
        <li>Online desktop as a service DaaS</li>
        <li>Disaster recovery as a service DRaaS</li>
        <li>Infrastructure as a service IaaS</li>
        <li>Backup as a service BaaS</li>
        <li>Integration / support</li>
      </ul>
    </div>
    <h2 class="band">Our solutions to your IT challenges</h2>
    <div class="panel-body">
      <h3 class="subhead">Online Desktop</h3>
      <p>Do you want to stop agonising about:</p>
      <ul class="bullets plain-list">
        <li>Your email systems and compliance?</li>
        <li>Your server hardware warranty?</li>
        <li>Your desktop software and patching levels?</li>
        <li>Software licensing?</li>
      </ul>
      <p>If you do, the Nimbara Online Desktop is for you. For a fixed price per month per user, you can move all your IT into our CLOUD and remove ALL YOUR ANXIETY. You'll know that your data is SAFE and SECURE in our two datacentres.</p>
      <p>And the best bit is this billing is month-to-month. You PAY for what you USE, no lock-in contracts – scale up or down depending on the amount of users in any given month.</p>
    </div>
    <div class="foot-strip"></div>
  </section>

  <section class="panel panel--feature">
    <div class="feature-top">
      <div class="feature-title">
        <h2>Backup and Disaster Recovery</h2>
        <div class="vault" role="img" aria-label="Illustration of a steel safe vault with a round dial"></div>
      </div>
      <h3 class="subhead">Backup:</h3>
      <p>Do you need to back up with a minimum amount of stress and reliance on tapes? Nimbara has the infrastructure to store backups of your data in a secure datacentre, accessible only by you. Just select the amount of storage required and we do the rest.</p>
      <p>An internet link is sufficient and you can back up to one of our world-class datacentres. As a further level of protection we mirror all your backups to our secondary datacentre to provide OPTIMUM REDUNDANCY.</p>
      <h3 class="subhead" style="margin-top:10px">Disaster Recovery:</h3>
      <p>Can you afford downtime on your production systems for any reason? Will your business suffer? These are the questions facing all small business owners today. There are some sobering statistics about data loss and business interruption. Nimbara disaster recovery solutions are elastically designed to be tailored to your business.</p>
      <ul class="bullets">
        <li>Redundancy across two datacentres</li>
        <li>Customised to your business</li>
        <li>Systems access by remote functionality if a DR situation develops</li>
        <li>Usage licensing – if the DR is not being used, cost to you is lower!</li>
      </ul>
    </div>
    <div class="network" role="img" aria-label="Illustration of computers and servers connected around a central cloud hub"></div>
    <p class="web">www.nimbara.com.au</p>
    <div class="foot-strip"></div>
  </section>

  <section class="panel panel--services">
    <h2 class="band" style="margin-top:40px">Infrastructure as a Service</h2>
    <div class="panel-body">
      <p>You've tried the public clouds like Stratus Web Services and Halcyon Vantor and have found the exact same problems as Nimbara did:</p>
      <ul class="ticks">
        <li><svg width="12" height="11" viewBox="0 0 12 11"><path d="M1 6l3.5 3.5L11 1" fill="none" stroke="var(--tick)" stroke-width="2.2"/></svg><span>Zero geometric benefit – they simply don't provide discount through volume image purchase.</span></li>
        <li><svg width="12" height="11" viewBox="0 0 12 11"><path d="M1 6l3.5 3.5L11 1" fill="none" stroke="var(--tick)" stroke-width="2.2"/></svg><span>No one to help.</span></li>
      </ul>
      <p>Nimbara understands. Our engineers can be hands-on or hands-off on your infrastructure in our public cloud – it's up to you.</p>
      <p>Our engineers can provide best practice implementations in a wide variety of fields including but not limited to:</p>
      <ul class="ticks ticks--short">
        <li><svg width="12" height="11" viewBox="0 0 12 11"><path d="M1 6l3.5 3.5L11 1" fill="none" stroke="var(--tick)" stroke-width="2.2"/></svg><span>Chatline</span></li>
        <li><svg width="12" height="11" viewBox="0 0 12 11"><path d="M1 6l3.5 3.5L11 1" fill="none" stroke="var(--tick)" stroke-width="2.2"/></svg><span>Mailhub</span></li>
        <li><svg width="12" height="11" viewBox="0 0 12 11"><path d="M1 6l3.5 3.5L11 1" fill="none" stroke="var(--tick)" stroke-width="2.2"/></svg><span>Docspace</span></li>
        <li><svg width="12" height="11" viewBox="0 0 12 11"><path d="M1 6l3.5 3.5L11 1" fill="none" stroke="var(--tick)" stroke-width="2.2"/></svg><span>SQL/File Clustering</span></li>
        <li><svg width="12" height="11" viewBox="0 0 12 11"><path d="M1 6l3.5 3.5L11 1" fill="none" stroke="var(--tick)" stroke-width="2.2"/></svg><span>Open Source load balancing</span></li>
        <li><svg width="12" height="11" viewBox="0 0 12 11"><path d="M1 6l3.5 3.5L11 1" fill="none" stroke="var(--tick)" stroke-width="2.2"/></svg><span>Open Source mail relaying to Mailhub</span></li>
      </ul>
      <p class="cta">If you need to build an infrastructure as a service cloud – let us help you!</p>
    </div>
    <h2 class="band" style="margin-top:14px">Integration and Support</h2>
    <div class="panel-body">
      <h3 class="subhead">Integration:</h3>
      <p>Nimbara offers full service network integration and support. We PLAN, DESIGN, DEPLOY and OPTIMISE IT Networks taking into consideration all aspects of your existing environment and developing the right solution to fit your needs.</p>
      <p>Our solutions deliver LAN, WAN and wireless connectivity between people, locations and systems both inside and outside your organisation.</p>
      <h3 class="subhead" style="margin-top:8px">Support:</h3>
      <p>Nimbara offers flexible and cost-effective support solutions. All provided from our Australian based support desk 24 hours a day, 365 days a year.</p>
    </div>
    <div class="foot-strip"></div>
  </section>

</main>
</body>
</html>
```